E-Book-Cover zum Thema künstliche Intelligenz
Zielgruppe
Angeboten wird ein kompaktes eBook über künstliche Intelligenz. Dem Leser soll die Funktionsweise künstlicher Intelligenz durch ein sehr einfaches Praxisbeispiel schnell und mühelos (ohne die Grundlagen ausführlich zu lernen) vermittelt werden.
Zielgruppe sind alle, die an dem Thema „Künstliche Intelligenz“ interessiert sind oder beruflich damit in Berührung kommen, die aber nicht zwingend Informatik studiert haben. Beispiele sind Studenten, Ingenieure, Manager, Unternehmer, Vertriebsangestellte, Techniker, Werbeleute, Mediziner, Online-Händler, interessierte Privatpersonen usw.
Aufgabenstellung
Das Cover sollte das Thema Künstliche Intelligenz darstellen. Es könnte beispielsweise ein neuronales Netz oder eine Roboterfigur verwendet werden. Auch Binärcode (1 und 0) oder elektronische Schaltungen könnten verwendet werden. Zudem sollte die Einfachheit betont werden. Wichtig ist mir, dass das Cover Aufmerksamkeit erzeugt professionell wirkt.
Das Cover sollte aus Vorderseite und Rücken bestehen.
Bildgröße sollte sein wie unter dem folgenden Link beschrieben: https://verlag.beispielhaus.de/de_DE/hilfe/thema/R481207736
Der Text sollte noch veränderbar sein.

```html
<!DOCTYPE html>
<html lang="de">
<head>
<meta charset="utf-8">
<title>Künstliche Intelligenz jetzt verstehen! – Rückseite</title>
<link rel="stylesheet" href="https://fonts.googleapis.com/css2?family=Exo+2:wght@300&family=Arimo:wght@400&display=swap">
<style>
  :root {
    --night: #020308;
    --glow-blue: #1c4778;
    --glow-deep: #0c1f3c;
    --steel-light: #c9d2de;
    --steel-mid: #7f8ea3;
    --circuit-blue: #5fc6ee;
    --copper: #7a4a2c;
    --text: #ffffff;
  }
  * { margin: 0; padding: 0; box-sizing: border-box; }
  html, body { width: 750px; height: 1200px; overflow: hidden; background: var(--night); }
  .back-cover {
    position: relative;
    width: 750px;
    height: 1200px;
    overflow: hidden;
    background:
      radial-gradient(ellipse 360px 520px at 230px 560px, var(--glow-blue) 0%, var(--glow-deep) 45%, rgba(2,3,8,0) 100%),
      radial-gradient(ellipse 500px 300px at 450px 900px, rgba(28,60,110,0.35) 0%, rgba(2,3,8,0) 100%),
      var(--night);
    color: var(--text);
    font-family: "Arimo", "Helvetica Neue", Arial, sans-serif;
  }
  .robot-visual {
    position: absolute;
    left: -60px;
    top: 40px;
    width: 380px;
    height: 1180px;
    background:
      radial-gradient(ellipse 110px 150px at 80px 170px, rgba(95,198,238,0.75) 0%, rgba(95,198,238,0.15) 70%, rgba(95,198,238,0) 100%),
      radial-gradient(ellipse 90px 90px at 110px 430px, rgba(122,74,44,0.8) 0%, rgba(122,74,44,0) 100%),
      radial-gradient(ellipse 200px 260px at 170px 700px, var(--steel-light) 0%, var(--steel-mid) 50%, rgba(127,142,163,0) 100%),
      radial-gradient(ellipse 160px 320px at 120px 1000px, rgba(127,142,163,0.45) 0%, rgba(127,142,163,0) 100%);
    opacity: 0.9;
  }
  .title {
    position: absolute;
    left: 218px;
    top: 72px;
    font-family: "Exo 2", "Rajdhani", sans-serif;
    font-weight: 300;
    font-size: 49px;
    line-height: 54px;
    letter-spacing: 0;
    white-space: nowrap;
  }
  .copy {
    position: absolute;
    left: 218px;
    width: 495px;
    font-size: 24px;
    line-height: 26px;
  }
  .copy .j { text-align: justify; text-align-last: justify; display: block; }
  .copy .l { display: block; }
  .feature-list {
    position: absolute;
    left: 269px;
    width: 440px;
    font-size: 24px;
    line-height: 26px;
    list-style: none;
  }
  .feature-list li { position: absolute; left: 0; padding-left: 17px; white-space: nowrap; }
  .feature-list li::before { content: "-"; position: absolute; left: 0; }
  .feature-list .continuation { position: absolute; left: 34px; white-space: nowrap; }
</style>
</head>
<body>
<main class="back-cover">
  <div class="robot-visual" role="img" aria-label="Fotografie eines weißen Roboters mit leuchtendem Schaltkreis-Kopf, seitlich angeschnitten"></div>

  <h1 class="title">Künstliche Intelligenz<br>jetzt verstehen!</h1>

  <p class="copy" style="top:225px">
    <span class="j">Wie funktioniert eigentlich künstliche Intelli-</span>
    <span class="l">genz?</span>
  </p>

  <p class="copy" style="top:290px">
    <span class="j">Das Thema Künstliche Intelligenz begegnet</span>
  </p>
  <p class="copy" style="top:329px">
    <span class="j">uns immer häufiger. Wir hören ständig davon</span>
    <span class="j">und nutzen sie bewusst oder unbewusst im</span>
    <span class="j">Alltag. Doch nur wenige wissen, wie die Tech-</span>
    <span class="j">nologie funktioniert und wie man sie praktisch</span>
    <span class="l">einsetzt.</span>
  </p>

  <p class="copy" style="top:471px">
    <span class="j">In diesem eBook zeige ich Ihnen die Entwick-</span>
  </p>
  <p class="copy" style="top:510px">
    <span class="j">lung und Nutzung künstlicher Intelligenz durch</span>
    <span class="j">ein anschauliches Beispiel. Im Beispiel ent-</span>
    <span class="j">wickeln wir einen virtuellen Arzt, der eine Vi-</span>
    <span class="j">rusgrippe (Influenza) diagnostizieren und von</span>
    <span class="j">einem harmlosen grippalen Infekt unterschie-</span>
    <span class="l">den soll.</span>
  </p>

  <p class="copy" style="top:679px">
    <span class="l">Dabei lernen Sie unter anderem:</span>
  </p>

  <ul class="feature-list" style="top:718px">
    <li style="top:0">Welche Daten eine KI benötigt und wie</li>
    <li class="continuation" style="top:39px; padding-left:0">man diese erfasst</li>
    <li style="top:70px">Wie ein künstliches neuronales Netz<br>durch Daten lernt</li>
    <li style="top:127px">Wie ein KI-Modell überprüft wird</li>
    <li style="top:153px">Wie man eine künstliche Intelligenz<br>praktisch einsetzt</li>
  </ul>
</main>
<style>
  .feature-list li.continuation::before { content: none; }
</style>
</body>
</html>
```